Tidewater Guest Consulting

I am an independent operator engaged on short/medium term consultancy briefs within the Hotel/Resort sector in the Pacific Area and have a representation in Fiji.

A broad based services is offered and includes:

Development Advisory
Property Management
Sales & Marketing
Holiday Ownership/Timeshare
Resorts/Apartments/Motels/Flashpackers/B&B
Financial & Legal Referrals

Industry/Entity Type

Hotel

Contact Information for Business Card

Business name - TIDEWATER GUEST CONSULTING
My name - Marcus Holt
Address: PO Box 318 Coral Heath 4871 Qld
Phone: Australia: +61 7 55019284 Mobile: 0414093857 (Viber)
Fiji: +679 8230519
Email: marcuswholt@tealnest-mail.com

```html
<!DOCTYPE html>
<html lang="en">
<head>
<meta charset="utf-8">
<title>Tidewater Guest Consulting – Business Card</title>
<link href="https://fonts.googleapis.com/css2?family=Arimo:wght@400;700&display=swap" rel="stylesheet">
<style>
  :root {
    --stage: #1d1d1f;
    --card-light: #ffffff;
    --card-shade: #d9d9d9;
    --brand-red: #ee3a3e;
    --ink: #2b2b2b;
    --ink-soft: #4a4a4a;
  }
  * { margin: 0; padding: 0; box-sizing: border-box; }
  html, body {
    width: 1200px;
    height: 908px;
    overflow: hidden;
    background: var(--stage);
    font-family: "Arimo", Arial, sans-serif;
  }
  .canvas {
    position: relative;
    width: 1200px;
    height: 908px;
    display: flex;
    flex-direction: column;
    align-items: center;
    justify-content: center;
    gap: 52px;
  }
  .card {
    position: relative;
    width: 600px;
    height: 343px;
    border-radius: 26px;
    overflow: hidden;
    background: radial-gradient(ellipse at 55% 35%, var(--card-light) 0%, #f1f1f1 45%, var(--card-shade) 100%);
  }
  /* Front side */
  .card-front .brand-line {
    position: absolute;
    inset: 0;
    display: flex;
    align-items: center;
    justify-content: center;
    color: var(--brand-red);
    font-weight: 700;
    font-size: 22px;
    letter-spacing: 4px;
  }
  /* Back side */
  .card-back .red-band {
    position: absolute;
    left: 0; right: 0; bottom: 0;
    height: 50px;
    background: var(--brand-red);
  }
  .brand-stack {
    position: absolute;
    right: 34px;
    top: 62px;
    text-align: right;
    color: var(--brand-red);
    font-weight: 700;
    font-size: 19px;
    line-height: 26px;
    letter-spacing: 3px;
  }
  .contact {
    position: absolute;
    left: 30px;
    top: 42px;
    color: var(--ink);
  }
  .identity {
    position: relative;
    padding-left: 14px;
  }
  .identity::before {
    content: "";
    position: absolute;
    left: 0; top: 2px;
    width: 4px;
    height: 40px;
    background: var(--brand-red);
  }
  .person-name { font-size: 19px; font-weight: 700; letter-spacing: 0.5px; }
  .person-title { font-size: 12px; color: var(--ink-soft); margin-top: 3px; }
  .reach { margin-top: 28px; font-size: 14px; line-height: 18px; color: var(--ink-soft); }
  .reach .phone { font-weight: 700; color: var(--ink); font-size: 15px; }
  .address { margin-top: 22px; font-size: 14px; line-height: 18px; color: var(--ink-soft); }
</style>
</head>
<body>
<main class="canvas">
  <section class="card card-front" aria-label="Business card front">
    <div class="brand-line">TIDEWATER GUEST CONSULTING</div>
  </section>

  <section class="card card-back" aria-label="Business card back">
    <div class="contact">
      <div class="identity">
        <div class="person-name">MARCUS HOLT</div>
        <div class="person-title">GENERAL MANAGER</div>
      </div>
      <div class="reach">
        <div class="phone">+61 7 55019284</div>
        <div class="email">marcuswholt@tealnest-mail.com</div>
        <div class="web">www.tidewaterguest.com</div>
      </div>
      <div class="address">
        <div>PO Box 318 Coral Heath,</div>
        <div>4871 Qld, Australia</div>
      </div>
    </div>
    <div class="brand-stack">
      <div>TIDEWATER</div>
      <div>GUEST</div>
      <div>CONSULTING</div>
    </div>
    <div class="red-band"></div>
  </section>
</main>
</body>
</html>
```